Private School Marketing Postcard

We are a commercial printing and mailing company. We are planning on starting a postcard mailing campaign targeted at private schools in Connecticut and Westchester County, NY. We are promoting our printing and mailing services and we are not sure how our postcards should be designed or what our advertising concept will be. We are looking for someone to come up with a postcard concept and design for our mailing campaign. (We will mail at least 3 versions in sequential mailings)

Target Market(s)

Private Schools

Industry/Entity Type

School

Font styles to use
Serif

Requirements
Must have
• Our Logo
• Harborlight Printing and Mailing, Inc.
• 47 Alder Street
• Norwalk, CT 06791
• www.harborlightprint.example
• 203.555.0148
• mark@harborlightprint.example
• Right half of side 2 must be blank for mailing panel

```html
<!DOCTYPE html>
<html lang="en">
<head>
<meta charset="utf-8">
<title>Harborlight Printing and Mailing – Postcard</title>
<link rel="stylesheet" href="https://fonts.googleapis.com/css2?family=Oswald:wght@300;400&family=Questrial&display=swap">
<style>
  :root{
    --stage:#2b2b2b;
    --cream:#fffbe0;
    --butter:#fdf1a8;
    --maroon:#8e1b1f;
    --maroon-dark:#6f1215;
    --ink:#222222;
    --cyan:#3ec3d6;
    --cyan-soft:#bfeaf0;
    --panel:#f1f1f1;
    --white:#ffffff;
    --badge:#1f5d84;
  }
  *{box-sizing:border-box;margin:0;padding:0}
  html,body{width:960px;height:1200px;overflow:hidden}
  body{background:var(--stage);position:relative;font-family:"Questrial",sans-serif;color:var(--ink)}

  .postcard{position:absolute;left:92px;width:774px;height:502px;overflow:hidden;background:var(--cream)}
  .postcard--front{top:70px}
  .postcard--back{top:632px;height:501px}
  .postcard__art{position:absolute;inset:0}

  .brand{position:absolute;display:flex;flex-direction:column;align-items:center}
  .brand__mark{width:58px;height:58px;border-radius:50%;border:5px solid var(--maroon)}
  .brand__name{margin-top:8px;font-family:"Questrial",sans-serif;font-size:26px;letter-spacing:4px;color:var(--ink);line-height:1}
  .brand__sub{margin-top:6px;font-family:"Questrial",sans-serif;font-size:9.5px;letter-spacing:2.2px;color:var(--ink);line-height:1}
  .postcard--front .brand{left:30px;top:26px;width:200px}
  .postcard--back .brand{left:36px;top:32px;width:200px}

  .tagline{position:absolute;left:0;top:170px;width:380px;height:98px;padding:14px 0 0 33px;
    background:linear-gradient(90deg,var(--cyan-soft) 0%,#d8f2f4 55%,rgba(255,255,255,0) 100%);
    font-family:"Oswald",sans-serif;font-weight:300;font-size:26px;line-height:38px;color:var(--ink)}
  .pitch{position:absolute;left:33px;top:298px;width:330px;font-family:"Oswald",sans-serif;font-weight:300;font-size:22.5px;line-height:37px;color:var(--maroon);white-space:nowrap}
  .web-line{position:absolute;left:33px;top:392px;display:flex;align-items:center;gap:8px;font-family:"Oswald",sans-serif;font-weight:300;font-size:16px;color:var(--ink)}
  .phone-band{position:absolute;left:0;top:440px;width:330px;height:42px;display:flex;align-items:center;gap:12px;padding-left:28px;
    background:linear-gradient(90deg,var(--cyan) 0%,#6fd3e0 65%,rgba(111,211,224,0) 100%);
    font-family:"Oswald",sans-serif;font-size:28px;color:var(--white)}
  .phone-band svg{flex:none}

  .badge{position:absolute;left:242px;top:37px;width:118px;height:44px;border-radius:4px;background:var(--badge);border:2px solid #cfdde6}

  .contact{position:absolute;left:42px;top:180px}
  .contact__title{font-family:"Questrial",sans-serif;font-size:28px;color:var(--maroon);margin-bottom:8px}
  .contact__row{display:flex;align-items:flex-start;gap:8px;font-size:20px;line-height:27px;color:var(--ink)}
  .contact__row svg{flex:none;margin-top:5px}
  .contact__row--indent{padding-left:26px}
  .social{position:absolute;left:46px;top:383px;display:flex;gap:13px}
  .social__dot{width:28px;height:28px;border-radius:50%;background:var(--ink)}
</style>
</head>
<body>

<section class="postcard postcard--front">
  <svg class="postcard__art" width="774" height="502" viewBox="0 0 774 502">
    <defs>
      <linearGradient id="frontCream" x1="0" y1="0" x2="1" y2="1">
        <stop offset="0" stop-color="#fffdf0"/>
        <stop offset="1" stop-color="#fdf0a4"/>
      </linearGradient>
      <linearGradient id="swatchTones" x1="0" y1="0" x2="1" y2="1">
        <stop offset="0" stop-color="#f4d0c8"/>
        <stop offset="0.3" stop-color="#e8a0b8"/>
        <stop offset="0.55" stop-color="#9fd2ea"/>
        <stop offset="0.8" stop-color="#c9b4e0"/>
        <stop offset="1" stop-color="#e6e6ee"/>
      </linearGradient>
      <linearGradient id="truckTones" x1="0" y1="0" x2="0" y2="1">
        <stop offset="0" stop-color="#f4f4f4"/>
        <stop offset="1" stop-color="#cfcfcf"/>
      </linearGradient>
    </defs>
    <rect width="774" height="502" fill="url(#frontCream)"/>
    <path d="M440 0 C410 90 372 170 382 260 C392 340 408 420 410 502 L774 502 L774 0 Z" fill="var(--maroon)"/>
    <g role="img" aria-label="Photo of colour swatch fan, colour charts and a printer's loupe">
      <path d="M456 0 C426 90 388 170 398 260 C406 340 420 420 422 502 L774 502 L774 0 Z" fill="url(#swatchTones)"/>
    </g>
    <g role="img" aria-label="Photo of a white mail delivery truck">
      <rect x="340" y="340" width="200" height="146" rx="10" fill="url(#truckTones)"/>
    </g>
  </svg>

  <div class="brand">
    <div class="brand__mark"></div>
    <div class="brand__name">HARBORLIGHT</div>
    <div class="brand__sub">PRINTING AND MAILING, INC.</div>
  </div>

  <div class="tagline">Commercial Printing with<br>Exceptional Service and Quality</div>

  <p class="pitch">Trust Harborlight Printing and Mailing, Inc.<br>With your next Project.</p>

  <div class="web-line">
    <svg width="18" height="18" viewBox="0 0 18 18" fill="none" stroke="var(--maroon)" stroke-width="1.5"><circle cx="9" cy="9" r="7.5"/><ellipse cx="9" cy="9" rx="3.2" ry="7.5"/><path d="M1.5 9h15M3 5h12M3 13h12"/></svg>
    <span>www.harborlightprint.example</span>
  </div>

  <div class="phone-band">
    <svg width="30" height="30" viewBox="0 0 30 30" fill="none" stroke="#fff" stroke-width="2"><circle cx="15" cy="15" r="13"/><path d="M10 8.5l3 3-1.5 2c1 2 2.5 3.5 4.5 4.5l2-1.5 3 3-2 2c-5 0-11-6-11-11z" fill="#fff" stroke="none"/></svg>
    <span>203.555.0148</span>
  </div>
</section>

<section class="postcard postcard--back">
  <svg class="postcard__art" width="774" height="501" viewBox="0 0 774 501">
    <defs>
      <linearGradient id="backCream" x1="0" y1="0" x2="1" y2="1">
        <stop offset="0" stop-color="#fffef6"/>
        <stop offset="1" stop-color="#fbeea0"/>
      </linearGradient>
    </defs>
    <rect width="774" height="501" fill="url(#backCream)"/>
    <path d="M460 0 C410 60 360 140 368 230 C374 320 450 370 456 434 L774 434 L774 0 Z" fill="var(--maroon)"/>
    <path d="M474 0 C426 62 378 140 384 230 C390 320 460 370 466 434 L774 434 L774 0 Z" fill="var(--panel)"/>
    <rect x="163" y="434" width="611" height="67" fill="var(--white)"/>
    <rect x="641" y="34" width="98" height="104" fill="none" stroke="var(--ink)" stroke-width="1.2"/>
    <g stroke="var(--ink)" stroke-width="1.2">
      <line x1="490" y1="275" x2="739" y2="275"/>
      <line x1="490" y1="310" x2="739" y2="310"/>
      <line x1="490" y1="347" x2="739" y2="347"/>
    </g>
  </svg>

  <div class="brand">
    <div class="brand__mark"></div>
    <div class="brand__name">HARBORLIGHT</div>
    <div class="brand__sub">PRINTING AND MAILING, INC.</div>
  </div>

  <div class="badge"></div>

  <div class="contact">
    <h2 class="contact__title">Contact Info</h2>
    <div class="contact__row">
      <svg width="16" height="20" viewBox="0 0 16 20" fill="none" stroke="var(--maroon)" stroke-width="1.8"><path d="M8 18s6-6.5 6-10.5A6 6 0 0 0 2 7.5C2 11.5 8 18 8 18z"/><circle cx="8" cy="7.5" r="2.2"/></svg>
      <span>47 Alder Street</span>
    </div>
    <div class="contact__row contact__row--indent">Norwalk, CT 06791</div>
    <div class="contact__row">
      <svg width="18" height="18" viewBox="0 0 18 18" fill="none" stroke="var(--maroon)" stroke-width="1.5"><circle cx="9" cy="9" r="7.5"/><ellipse cx="9" cy="9" rx="3.2" ry="7.5"/><path d="M1.5 9h15M3 5h12M3 13h12"/></svg>
      <span>www.harborlightprint.example</span>
    </div>
    <div class="contact__row">
      <svg width="18" height="18" viewBox="0 0 30 30" fill="none" stroke="var(--maroon)" stroke-width="2.4"><circle cx="15" cy="15" r="13"/><path d="M10 8.5l3 3-1.5 2c1 2 2.5 3.5 4.5 4.5l2-1.5 3 3-2 2c-5 0-11-6-11-11z" fill="var(--maroon)" stroke="none"/></svg>
      <span>203.555.0148</span>
    </div>
    <div class="contact__row">
      <svg width="18" height="18" viewBox="0 0 18 14" fill="none" stroke="var(--maroon)" stroke-width="1.4"><rect x="1" y="1.5" width="16" height="11"/><path d="M1 1.5l8 6 8-6"/></svg>
      <span>mark@harborlightprint.example</span>
    </div>
  </div>

  <div class="social" aria-hidden="true">
    <span class="social__dot"></span><span class="social__dot"></span><span class="social__dot"></span>
    <span class="social__dot"></span><span class="social__dot"></span><span class="social__dot"></span>
  </div>
</section>

</body>
</html>
```